Business Card Design Project

We need a business card design for a new company based in New York called "Marble Fox's". We do major installations of energy saving devices primarily LED lighting in large facilities. We would like a double sided card with our contact info on one side with our logo (to be designed) and on the other side the services we provide. We would like a heavy weight glossy card using the colors green and white. The final design should communicate environmental soundness and our market is very upscale corporations.
We would like our logo to illustrate LED lighting and we were thinking if we could get a stock picture of the Corliss Vane Building lit up on July 4th with red, white and blue LED lighting. The alternative would be anything that connotes environmentally proper thinking. It could be either a picture or a design.

```html
<!DOCTYPE html>
<html lang="en">
<head>
<meta charset="utf-8">
<title>Marble Fox's – Business Card</title>
<link rel="stylesheet" href="https://fonts.googleapis.com/css2?family=Quicksand:wght@300;400;500;700&display=swap">
<style>
  :root {
    --green: #8dc03f;
    --green-deep: #79b530;
    --white: #ffffff;
    --backdrop: #e9ebe7;
  }
  * { margin: 0; padding: 0; box-sizing: border-box; }
  html, body {
    width: 1200px;
    height: 1200px;
    overflow: hidden;
    background: var(--backdrop);
    font-family: "Quicksand", sans-serif;
  }
  .canvas { position: relative; width: 1200px; height: 1200px; }

  .card {
    position: absolute;
    left: 178px;
    width: 841px;
    height: 461px;
    background: var(--white);
    overflow: hidden;
    box-shadow: 0 2px 10px rgba(0,0,0,0.12);
  }
  .card--front { top: 94px; }
  .card--back { top: 625px; }

  /* Front */
  .brand-mark {
    position: absolute;
    left: 362px;
    top: 156px;
    width: 110px;
    height: 110px;
    border-radius: 50%;
    background: var(--green);
  }
  .brand-name {
    position: absolute;
    left: 0;
    right: 0;
    top: 284px;
    text-align: center;
    font-weight: 700;
    font-size: 66px;
    line-height: 1;
    color: var(--green);
  }
  .brand-tagline {
    position: absolute;
    left: 0;
    right: 0;
    top: 372px;
    text-align: center;
    font-weight: 500;
    font-size: 14px;
    letter-spacing: 0.5px;
    color: var(--green);
  }

  /* Back */
  .services {
    position: absolute;
    left: 50px;
    width: 650px;
    top: 84px;
    text-align: center;
    font-weight: 500;
    font-size: 23px;
    line-height: 31px;
    letter-spacing: 1.2px;
    color: var(--green);
  }
  .contact-band {
    position: absolute;
    left: 0;
    top: 259px;
    width: 418px;
    height: 158px;
    background: var(--green);
    color: var(--white);
  }
  .contact-band__notch {
    position: absolute;
    left: 0;
    top: 16px;
    width: 22px;
    height: 40px;
  }
  .contact-name {
    position: absolute;
    left: 33px;
    top: 17px;
    font-weight: 400;
    font-size: 31px;
    line-height: 38px;
  }
  .contact-list {
    position: absolute;
    left: 70px;
    top: 67px;
    list-style: none;
    font-weight: 500;
    font-size: 13px;
    line-height: 27px;
  }
  .decor-circle {
    position: absolute;
    left: 625px;
    top: 182px;
    width: 214px;
    height: 214px;
    border-radius: 50%;
    background: var(--green-deep);
  }
</style>
</head>
<body>
<main class="canvas">
  <section class="card card--front" aria-label="Card front">
    <div class="brand-mark" aria-hidden="true"></div>
    <h1 class="brand-name">Marble Fox's</h1>
    <p class="brand-tagline">Energy Saving Services</p>
  </section>

  <section class="card card--back" aria-label="Card back">
    <p class="services">Install energy saving devices primarily LED<br>lighting for large facilities</p>

    <div class="contact-band">
      <svg class="contact-band__notch" viewBox="0 0 22 40" aria-hidden="true">
        <polygon points="0,0 20,20 0,40" fill="#ffffff"/>
      </svg>
      <h2 class="contact-name">Dana Whitlow</h2>
      <ul class="contact-list">
        <li>555 210 447</li>
        <li>4120 Linden Avenue Albany, NY 12203</li>
        <li>hello@marblefoxs.com</li>
      </ul>
    </div>

    <div class="decor-circle" aria-hidden="true"></div>
  </section>
</main>
</body>
</html>
```